Design a scratch lotto card

Developping 2 lottery scratch card colors of preference: gold, yellow, green and blue. Size 5x3. Name of the cards are "DUX ORLO" and ''GLIMBO ORLO''. I want the card to be eyecatching and some dollar signs. would also prefer no writing just the name and design

Target Market(s)

people who like gambling

Colors
0792cd
33a6d7
3276b5
fbee3e
fbed22
fece3e
fbf289
9bcb3b
fefdec

Requirements
Must have
• colors mentionned and empty blank center space where grid will go
Nice to have
• cash or gold touches

```html
<!DOCTYPE html>
<html lang="en">
<head>
<meta charset="utf-8">
<title>Scratch Lotto Cards</title>
<link href="https://fonts.googleapis.com/css2?family=Anton&display=swap" rel="stylesheet">
<style>
  :root {
    --backdrop: #7d7d7d;
    --green-deep: #3f8a1e;
    --green-mid: #6fb23a;
    --green-light: #9bcb3b;
    --green-band: #19a64d;
    --cream: #fbf6d4;
    --gold-dark: #c09a2a;
    --gold-light: #f0d56a;
    --yellow: #fbee3e;
    --yellow-soft: #fbf289;
    --white: #fefdec;
    --silver-dark: #8e8e8e;
    --silver-light: #e6e6e6;
  }
  html, body {
    margin: 0;
    width: 1200px;
    height: 1200px;
    overflow: hidden;
    background: var(--backdrop);
  }
  .canvas {
    position: relative;
    width: 1200px;
    height: 1200px;
  }
  .card {
    position: absolute;
    left: 100px;
    width: 1000px;
    height: 540px;
    display: block;
    box-shadow: 0 10px 24px rgba(0,0,0,0.35);
  }
  .card--dux { top: 50px; }
  .card--glimbo { top: 620px; }
  .title-text {
    font-family: 'Anton', sans-serif;
    letter-spacing: 1px;
  }
  .card-name {
    font-family: 'Anton', sans-serif;
  }
  .dollar {
    font-family: 'Anton', sans-serif;
    paint-order: stroke;
    stroke: var(--white);
    stroke-linejoin: round;
  }
</style>
</head>
<body>
<main class="canvas">

  <!-- Card one: green ticket -->
  <svg class="card card--dux" viewBox="0 0 1000 540" xmlns="http://www.w3.org/2000/svg">
    <defs>
      <linearGradient id="duxBorder" x1="0" y1="0" x2="1" y2="1">
        <stop offset="0" stop-color="#78b83e"/>
        <stop offset="1" stop-color="#5fa431"/>
      </linearGradient>
      <linearGradient id="goldTitle" x1="0" y1="0" x2="0" y2="1">
        <stop offset="0" stop-color="#f6e27a"/>
        <stop offset="0.5" stop-color="#d6ac2e"/>
        <stop offset="1" stop-color="#b7861c"/>
      </linearGradient>
      <linearGradient id="silverBar" x1="0" y1="0" x2="1" y2="0">
        <stop offset="0" stop-color="var(--silver-dark)"/>
        <stop offset="0.45" stop-color="var(--silver-light)"/>
        <stop offset="1" stop-color="var(--silver-dark)"/>
      </linearGradient>
      <linearGradient id="pigArea" x1="0" y1="0" x2="0" y2="1">
        <stop offset="0" stop-color="#f4b596"/>
        <stop offset="0.7" stop-color="#e9a07c"/>
        <stop offset="1" stop-color="#e2bd3c"/>
      </linearGradient>
    </defs>

    <rect class="card-base" width="1000" height="540" fill="url(#duxBorder)"/>

    <path class="ticket-panel"
      d="M110 130 Q150 130 150 95 L860 95 Q860 135 905 135 L905 420 Q860 420 860 460 L150 460 Q150 420 110 420 Z"
      fill="var(--cream)" stroke="var(--green-light)" stroke-width="12"/>

    <path class="top-crest" d="M310 60 L690 60 Q690 180 500 185 Q310 180 310 60 Z"
      fill="var(--green-mid)" stroke="var(--green-light)" stroke-width="10"/>
    <ellipse class="crest-ornament" role="img" aria-label="Leafy winged ornament"
      cx="500" cy="118" rx="95" ry="50" fill="#8fc85a"/>

    <path class="bottom-mound" d="M470 540 Q470 390 720 385 L980 385 L980 540 Z"
      fill="var(--green-mid)" stroke="var(--green-light)" stroke-width="10"/>

    <rect class="hero-illustration" role="img"
      aria-label="Cheerful piggy bank standing on stacks of gold coins with banknotes flying around"
      x="700" y="110" width="230" height="260" rx="30" fill="url(#pigArea)"/>

    <text class="title-text" x="130" y="270" font-size="120" fill="url(#goldTitle)"
      stroke="var(--yellow)" stroke-width="2" textLength="440" lengthAdjust="spacingAndGlyphs">SCRATCH</text>
    <text class="title-text" x="150" y="390" font-size="120" fill="url(#goldTitle)"
      stroke="var(--yellow)" stroke-width="2">&amp; WIN</text>

    <text class="card-name" x="540" y="430" font-size="40" fill="var(--yellow)">DUX ORLO</text>
    <rect class="scratch-bar" x="520" y="445" width="330" height="58" rx="12"
      fill="url(#silverBar)" stroke="var(--white)" stroke-width="3"/>
  </svg>

  <!-- Card two: gold and green -->
  <svg class="card card--glimbo" viewBox="0 0 1000 540" xmlns="http://www.w3.org/2000/svg">
    <defs>
      <linearGradient id="goldTop" x1="0" y1="0" x2="1" y2="0">
        <stop offset="0" stop-color="var(--gold-dark)"/>
        <stop offset="0.45" stop-color="var(--gold-light)"/>
        <stop offset="1" stop-color="var(--gold-dark)"/>
      </linearGradient>
      <linearGradient id="greenBand" x1="0" y1="0" x2="1" y2="0">
        <stop offset="0" stop-color="var(--green-band)"/>
        <stop offset="0.5" stop-color="var(--green-light)"/>
        <stop offset="1" stop-color="var(--green-band)"/>
      </linearGradient>
      <linearGradient id="titleGlow" x1="0" y1="0" x2="0" y2="1">
        <stop offset="0" stop-color="#2f9a2c"/>
        <stop offset="0.5" stop-color="var(--yellow)"/>
        <stop offset="1" stop-color="#2f9a2c"/>
      </linearGradient>
      <linearGradient id="silverBar2" x1="0" y1="0" x2="1" y2="0">
        <stop offset="0" stop-color="var(--silver-dark)"/>
        <stop offset="0.5" stop-color="var(--silver-light)"/>
        <stop offset="1" stop-color="var(--silver-dark)"/>
      </linearGradient>
    </defs>

    <rect class="gold-field" width="1000" height="540" fill="url(#goldTop)"/>
    <rect class="green-band" y="270" width="1000" height="270" fill="url(#greenBand)"/>

    <g class="dollar-cluster">
      <text class="dollar" x="410" y="200" font-size="190" fill="#8fbf3c" stroke-width="14">$</text>
      <text class="dollar" x="540" y="240" font-size="130" fill="#5e9d24" stroke-width="12">$</text>
      <text class="dollar" x="620" y="245" font-size="125" fill="#3f8a1e" stroke-width="12">$</text>
      <text class="dollar" x="270" y="262" font-size="110" fill="#4d9420" stroke-width="12">$</text>
      <text class="dollar" x="340" y="250" font-size="125" fill="#9bcb3b" stroke-width="12">$</text>
      <text class="dollar" x="420" y="262" font-size="140" fill="#2f6b10" stroke-width="12">$</text>
      <text class="dollar" x="500" y="262" font-size="110" fill="#8fbf3c" stroke-width="12">$</text>
    </g>

    <text class="title-text" x="170" y="400" font-size="125" fill="url(#titleGlow)"
      stroke="var(--yellow)" stroke-width="3" textLength="780" lengthAdjust="spacingAndGlyphs">SCRATCH &amp; WIN</text>

    <rect class="scratch-bar" x="590" y="420" width="360" height="56" rx="12"
      fill="url(#silverBar2)" stroke="var(--white)" stroke-width="3"/>

    <text class="card-name" x="180" y="500" font-size="58" fill="var(--white)">GLIMBO ORLO</text>
  </svg>

</main>
</body>
</html>
```